North Fern Holdings Business Card

A business card design to accompany the logo design you completed on Artisan Hive. We are open to your proposals. I did add one idea below that might work, but we aren't married to the idea. The company is a real estate services company. Clientele are typically high net worth individuals, executive level employment or owners of their own company, 30-60 years old.

Our 1 (bad?) idea: double sided card; One side landscape with logo and word mark. Other side Portrait with the logo only (oversize watermark maybe?). Somewhere add text of Name (Marcus Pellington), Title (Principal), phone # (949-555-0173) and email address (marcus@northfernhq.com). There would be a second design with my wife's name, number and email in place of mine.

Again totally open to ideas here.

Industry/Entity Type

Real Estate

```html
<!DOCTYPE html>
<html lang="en">
<head>
<meta charset="utf-8">
<title>North Fern Holdings – Business Card</title>
<link rel="stylesheet" href="https://fonts.googleapis.com/css2?family=Arimo:wght@400&display=swap">
<style>
  :root {
    --stage: #1c1c1c;
    --fern: #5ea64e;
    --paper: #ffffff;
    --mist: #eef0ec;
    --ink-on-fern: #ffffff;
    --ink: #333333;
  }
  * { margin: 0; padding: 0; box-sizing: border-box; }
  html, body {
    width: 1200px; height: 900px; overflow: hidden;
    background: var(--stage);
  }
  .stage { position: relative; width: 1200px; height: 900px; }
  .card {
    position: absolute;
    overflow: hidden;
    border-radius: 4px;
    font-family: 'Arimo', Arial, sans-serif;
  }

  /* Brand name: one line, one weight of the card's text face */
  .brand-name {
    position: absolute; left: 0; right: 0;
    display: flex; align-items: center; justify-content: center;
    font-family: 'Arimo', Arial, sans-serif;
    font-weight: 400;
    line-height: 1;
    white-space: nowrap;
  }
  .brand-name__square {
    display: inline-block; background: currentColor; flex: none;
  }

  /* Front: landscape */
  .card--front {
    left: 90px; top: 290px; width: 560px; height: 320px;
    background: var(--fern);
  }
  .card--front .watermark {
    position: absolute; left: -40px; top: -60px; width: 320px; height: 320px;
    border-radius: 50%;
    background: radial-gradient(circle, rgba(255,255,255,0.10), rgba(255,255,255,0) 70%);
  }
  .card--front .brand-name {
    top: 142px; font-size: 34px; gap: 14px;
    color: var(--ink-on-fern);
  }
  .card--front .brand-name__square { width: 16px; height: 16px; }

  /* Back: portrait */
  .card--back {
    left: 760px; top: 170px; width: 320px; height: 560px;
    background: var(--paper);
  }
  .card--back .watermark {
    position: absolute; left: 40px; top: 20px; width: 300px; height: 320px;
    border-radius: 40% 40% 50% 50%;
    background: radial-gradient(ellipse at 50% 45%, var(--mist), rgba(238,240,236,0) 72%);
  }
  .card--back .brand-name {
    top: 168px; font-size: 22px; gap: 9px;
    color: var(--fern);
  }
  .card--back .brand-name__square { width: 11px; height: 11px; }

  .name-band {
    position: absolute; left: 0; right: 0; top: 300px; height: 78px;
    background: var(--fern);
    color: var(--ink-on-fern);
    text-align: center;
    padding-top: 16px;
  }
  .name-band__name  { display: block; font-size: 21px; line-height: 1.2; }
  .name-band__title { display: block; font-size: 14px; margin-top: 5px; line-height: 1.2; }

  .contact {
    position: absolute; left: 52px; top: 420px;
    list-style: none;
    font-size: 14px; color: var(--ink);
  }
  .contact li { display: flex; align-items: center; gap: 9px; margin-bottom: 16px; }
  .contact svg { width: 16px; height: 16px; fill: var(--fern); flex: none; }
</style>
</head>
<body>
<main class="stage">

  <section class="card card--front" aria-label="Card front">
    <div class="watermark" role="img" aria-label="Faint oversize brand emblem watermark"></div>
    <p class="brand-name"><span class="brand-name__square"></span>North Fern Holdings</p>
  </section>

  <section class="card card--back" aria-label="Card back">
    <div class="watermark" role="img" aria-label="Faint oversize brand emblem watermark"></div>
    <p class="brand-name"><span class="brand-name__square"></span>North Fern Holdings</p>

    <div class="name-band">
      <span class="name-band__name">Marcus Pellington</span>
      <span class="name-band__title">Principal</span>
    </div>

    <ul class="contact">
      <li>
        <svg viewBox="0 0 24 24" aria-hidden="true"><path d="M6.6 10.8a15.1 15.1 0 0 0 6.6 6.6l2.2-2.2a1 1 0 0 1 1-.25 11.4 11.4 0 0 0 3.6.57 1 1 0 0 1 1 1V20a1 1 0 0 1-1 1A17 17 0 0 1 3 4a1 1 0 0 1 1-1h3.5a1 1 0 0 1 1 1c0 1.25.2 2.45.57 3.57a1 1 0 0 1-.25 1z"/></svg>
        <span>949-555-0173</span>
      </li>
      <li>
        <svg viewBox="0 0 24 24" aria-hidden="true"><path d="M2 5h20v14H2z M4 7v.5l8 5 8-5V7l-8 5z" fill-rule="evenodd"/></svg>
        <span>marcus@northfernhq.com</span>
      </li>
    </ul>
  </section>

</main>
</body>
</html>
```